New Vegan Documentary Film Needs Poster Design

We are developing a documentary film production project called "Orchard Without Reckoning: A Quiet Weight Beneath Every Choice."

The documentary will explore the numerous consequences of our practice of commodifying animals for food. These consequences include:

* Cultural impact (global hunger, conflict and war, disease and health epidemics, waste.)
* Ecological toll (soil erosion, water &air pollution, rain forest devastation, global warming, species extinction, ocean destruction, etc.)
* Economic devastation (dependency on resources, health care & pharmaceutical/medical industry.)
Historical issues (cultural aggression, rise of the elite, slavery, domination of women.)
* Personal psyche (commodification of life, disconnectedness from and repression of our innate compassionate nature, intelligence, and sense of justice.)

The film will represent the ideals of kindness, justice, and freedom, and educate on the the keys to awakening from the invisible cultural food trance, and overall, be a vehicle to encourage awakening and living with awareness.

As per the film's title, we want the poster to convey the multi-layered global consequences of animal agriculture without openly attacking the meat industry or people eating animal-sourced foods.

This is a mass-appeal documentary intended to open the eyes of the general public without judgment or alienation of any sector of society. This is not about blame; it's about awareness. The poster should convey the same non-judgmental perspective.

Format should be standard film poster.
Copy for the poster must include the title, sub-title and a quote
Title: Orchard Without Reckoning:
Sub-title: A Quiet Weight Beneath Every Choice
Quote options (Pick one) -
As we sow, so shall we reap.
Question everything.
We are all in this together.
None of us is completely innocent.

```html
<!DOCTYPE html>
<html lang="en">
<head>
<meta charset="utf-8">
<title>Orchard Without Reckoning – Film Poster</title>
<link rel="stylesheet" href="https://fonts.googleapis.com/css2?family=Anton&family=Oswald:wght@600;700&family=Arimo:wght@700&display=swap">
<style>
  :root {
    --stage: #d9dcdd;
    --poster-teal: #0c6f8a;
    --poster-teal-deep: #0a5a70;
    --treeline: #23402f;
    --field-light: #4f7d5a;
    --field-green: #3f6b4c;
    --field-dark: #1d3324;
    --night: #050807;
    --title-white: #f4f5f2;
    --subtitle-yellow: #d9e021;
    --quote-white: #ffffff;
    --placeholder-line: rgba(255, 255, 255, 0.28);
  }
  * { margin: 0; padding: 0; box-sizing: border-box; }
  html, body {
    width: 1200px;
    height: 1000px;
    overflow: hidden;
    background: var(--stage);
  }
  .canvas {
    width: 1200px;
    height: 1000px;
    display: flex;
    align-items: center;
    justify-content: center;
  }
  .poster {
    position: relative;
    width: 634px;
    height: 940px;
    overflow: hidden;
    background: linear-gradient(180deg, var(--poster-teal) 0%, var(--poster-teal-deep) 40%, var(--night) 100%);
  }
  .poster-photo {
    position: absolute;
    left: 0;
    right: 0;
    top: 345px;
    height: 595px;
    background:
      radial-gradient(ellipse 60% 30% at 45% 42%, rgba(150, 95, 45, 0.45), transparent 70%),
      radial-gradient(ellipse 45% 22% at 40% 64%, rgba(0, 0, 0, 0.55), transparent 75%),
      linear-gradient(180deg,
        var(--treeline) 0%,
        var(--treeline) 4%,
        var(--field-light) 6%,
        var(--field-green) 22%,
        #35593f 40%,
        var(--field-dark) 62%,
        #0b120d 80%,
        var(--night) 100%);
  }
  .poster-photo::after {
    content: "";
    position: absolute;
    inset: 18px 18px 230px 18px;
    border: 2px dashed var(--placeholder-line);
  }
  .poster-title-block {
    position: absolute;
    top: 128px;
    left: 0;
    right: 0;
    text-align: center;
  }
  .poster-title {
    font-family: "Anton", "Oswald", sans-serif;
    font-weight: 400;
    color: var(--title-white);
    font-size: 72px;
    line-height: 1;
    letter-spacing: 0.5px;
    text-transform: uppercase;
    text-shadow: 3px 3px 0 rgba(0, 0, 0, 0.5);
  }
  .poster-title span { display: block; }
  .poster-subtitle {
    margin-top: 8px;
    font-family: "Oswald", sans-serif;
    font-weight: 700;
    color: var(--subtitle-yellow);
    font-size: 25px;
    letter-spacing: 0.3px;
    text-transform: uppercase;
  }
  .poster-quote {
    position: absolute;
    left: 0;
    right: 0;
    top: 700px;
    text-align: center;
    font-family: "Arimo", "Arial", sans-serif;
    font-weight: 700;
    color: var(--quote-white);
  }
  .poster-quote .quote-lead {
    display: block;
    font-size: 40px;
    line-height: 1.1;
    letter-spacing: -0.5px;
  }
  .poster-quote .quote-emphasis {
    display: block;
    font-size: 54px;
    line-height: 1.05;
    letter-spacing: 1px;
  }
</style>
</head>
<body>
  <main class="canvas">
    <article class="poster">
      <div class="poster-photo" role="img" aria-label="Photograph of brown and white cattle grazing and resting in a green pasture below a treeline, with a large dark cow lying in the foreground fading into black"></div>

      <header class="poster-title-block">
        <h1 class="poster-title"><span>Orchard Without</span><span>Reckoning</span></h1>
        <p class="poster-subtitle">A Quiet Weight Beneath Every Choice</p>
      </header>

      <p class="poster-quote">
        <span class="quote-lead">We are all in this</span>
        <span class="quote-emphasis">TOGETHER</span>
      </p>
    </article>
  </main>
</body>
</html>
```